Wine Label designs

I need a nice- upper class wine label made. I would like a black or dark background matte finish with gold foil text and the outline. 4386 in the middle in bold & gold. I want to it be Detroit themed. With the Cal Brenner fist or herald of Varnost statue or both small in a step and repeat embossed black on the matte black label. All of the label with fists. The name of the brand is 4386. The name comes from when Detroit was founded. This label will be for a red win.

Target Market(s)

Wine drinkers & Detroit Michigan themed background

Industry/Entity Type

Wine

Logo Text

4386

Logo styles of interest
Wordmark Logo
Requirements
Must have
• The color Gold
Nice to have
• Matte finish and Gold out line & gold text

```html
<!DOCTYPE html>
<html lang="en">
<head>
<meta charset="utf-8">
<title>4386 Wine Label</title>
<link href="https://fonts.googleapis.com/css2?family=Playfair+Display:wght@700&family=Old+Standard+TT:wght@700&display=swap" rel="stylesheet">
<style>
  :root {
    --backdrop: #5f605e;
    --label-black: #141214;
    --label-black-soft: #1e1c1e;
    --gold-dark: #a58e66;
    --gold-light: #e9d5a8;
    --gold-mid: #c4ac7f;
    --gold-text: #d2bd8e;
    --paper: #ffffff;
    --ink: #1b1a1b;
  }
  * { margin: 0; padding: 0; box-sizing: border-box; }
  html, body { width: 802px; height: 1200px; overflow: hidden; }
  body { background: var(--backdrop); position: relative; }

  .neck-label {
    position: absolute; left: 33px; top: 672px; width: 185px; height: 235px;
    display: flex; flex-direction: column;
  }
  .neck-label__top { flex: 0 0 148px; background: var(--label-black-soft); }
  .neck-label__band {
    flex: 1;
    background: linear-gradient(90deg, var(--gold-dark), var(--gold-mid) 55%, var(--gold-light) 85%, var(--gold-mid));
    display: flex; align-items: center; justify-content: center;
  }
  .neck-label__name {
    font-family: "Playfair Display", serif; font-weight: 700;
    font-size: 32px; color: var(--ink); letter-spacing: 0.5px; margin-top: 14px;
  }

  .body-label {
    position: absolute; left: 382px; top: 278px; width: 388px; height: 645px;
    display: flex; flex-direction: column;
  }
  .body-label__crest {
    flex: 0 0 21px;
    background: linear-gradient(90deg, var(--gold-dark), var(--gold-light) 70%, var(--gold-mid));
  }
  .body-label__panel {
    flex: 0 0 454px; position: relative;
    background: linear-gradient(180deg, #141114 0%, var(--label-black) 50%, #18161a 100%);
    display: flex; align-items: center; justify-content: center;
  }
  .body-label__name {
    font-family: "Playfair Display", serif; font-weight: 700;
    font-size: 96px; line-height: 1; color: var(--gold-text); margin-top: 54px;
  }
  .body-label__notes {
    flex: 0 0 136px; background: var(--paper);
    padding: 27px 34px 0;
    font-family: "Old Standard TT", serif; font-weight: 700;
    font-size: 9px; line-height: 1.45; color: var(--ink); text-align: center;
  }
  .body-label__footer {
    flex: 1;
    background: linear-gradient(90deg, var(--gold-dark), var(--gold-mid) 50%, var(--gold-light) 75%, var(--gold-mid));
  }
</style>
</head>
<body>
  <div class="neck-label">
    <div class="neck-label__top"></div>
    <div class="neck-label__band">
      <span class="neck-label__name">4386</span>
    </div>
  </div>

  <div class="body-label">
    <div class="body-label__crest" role="img" aria-label="Gold sawtooth edge along the top of the label"></div>
    <div class="body-label__panel" role="img" aria-label="Matte black field with a fine gold triangular line pattern">
      <span class="body-label__name">4386</span>
    </div>
    <p class="body-label__notes">Lorem ipsum dolor sit amet, consectetuer adipiscing elit, sed diam nonummy nibh euismod tincidunt ut laoreet dolore magna aliquam erat volutpat. Ut wisi enim ad minim veniam, quis nostrud exerci tation ullamcorper suscipit</p>
    <div class="body-label__footer"></div>
  </div>
</body>
</html>
```